Law Firm Web Design Project

I need a website design for my law firm. I have attached to this description the URL of a website I liked with a description of the elements of that website that appeal to me.

I am also attaching my law firm's logo, so you can review that design when you create the website design.

Reference Site: www.harborfamilycounselpros.com

What we like about this site:
• The different layers
• Subtle designs, textures, curves
• 3 dimensional
• Floating effect
• Simple logo that stands out (we are providing logo)
• Prominent phone number
• Location of Areas of Practice
oDivorce, Legal Separation, Paternity, Spousal Maintenance, Child Custody, Child Support, Protective Orders, Community Property, Business Evaluations
• The limited amount of links across the top
o Home, Meet Our Attorney, FAQ, Contact Us
• Request A Consultation click through
• Right side bar with the moving icons
• Badges

Other Tips:
• We don’t want the website to be dark. The logo can standout and the website can have its own colors and flow.
• We would like there to be a “call to action” or way to get in touch on every page and every page view
• We would like a place for credit card icons at the bottom of the page
• Strong, yet elegant
• Finally, just use the website provided as a guide. Explore different colors, textures, shapes, shadows etc.
Updates

I would prefer the website have colors that are complementary to my logo and that are strong and elegant.  I like black, gold, amber, and tan colors.  Black should be used sparingly as an accent only, since I don't want the website to be too dark.

Please review the website I provided as an example in my project description.  I really like the three dimensional aspects of that website (web page floating on top of a background and the logo in the upper left floating on top of the web page).  I also like the use of "swirling" on the background and the webpage.  I hope this additional information is helpful.

Requirements
Must have
• I need a place to insert "client testimonials", a place to insert four logos of awards the law firm has received, a place for people to fill out a form to contact the law firm via email, and a place for people to click to review articles I have written.

```html
<!DOCTYPE html>
<html lang="en">
<head>
<meta charset="utf-8">
<title>Whitmore Law – Family Law Attorney</title>
<link rel="stylesheet" href="https://fonts.googleapis.com/css2?family=Gelasio:wght@400&family=Source+Sans+3:wght@400;600&display=swap">
<style>
  :root {
    --gold: #a8893a;
    --gold-light: #dcc25e;
    --gold-mid: #c6a744;
    --gold-dark: #7e6524;
    --ink: #2b2b2b;
    --text: #4a4a4a;
    --rule: #d6d6d6;
    --panel: #ffffff;
    --page: #f1f1f1;
    --field-border: #b9b9b9;
  }
  * { box-sizing: border-box; margin: 0; padding: 0; }
  html, body { width: 979px; height: 1200px; overflow: hidden; }
  body {
    position: relative;
    background: radial-gradient(ellipse at 120px 60px, #ffffff 0%, #f4f4f4 40%, #ececec 100%);
    font-family: "Source Sans 3", "Myriad Pro", sans-serif;
    color: var(--text);
  }
  .abs { position: absolute; }
  .serif { font-family: "Gelasio", Georgia, serif; font-weight: 400; }

  /* header */
  .header-band { left: 40px; top: 0; width: 905px; height: 66px; }
  .brand { left: 44px; top: 30px; display: flex; align-items: center; gap: 14px; }
  .brand-mark { width: 46px; height: 46px; background: var(--ink); border: 3px solid var(--gold); }
  .brand-name { font-family: "Gelasio", Georgia, serif; font-size: 31px; color: var(--gold); letter-spacing: 0.5px; }
  .main-nav { left: 548px; top: 20px; display: flex; height: 26px; align-items: center; }
  .main-nav a { color: var(--ink); text-decoration: none; font-size: 14.5px; padding: 0 16px; line-height: 26px; border-left: 1px solid var(--gold-dark); }
  .main-nav a:first-child { border-left: none; }

  /* sidebar */
  .practice-title { left: 40px; top: 117px; width: 254px; height: 32px; background: linear-gradient(#b0923f, #9d8032); color: #2d2510; font-size: 17.5px; padding: 4px 0 0 15px; }
  .practice-list { left: 56px; top: 161px; list-style: none; }
  .practice-list li { font-size: 13px; color: var(--ink); height: 23px; line-height: 20px; }

  .quick-contact { left: 40px; top: 793px; width: 235px; height: 270px; background: var(--panel); border-radius: 8px; box-shadow: 0 1px 4px rgba(0,0,0,0.08); }
  .quick-title { left: 7px; top: 8px; width: 220px; height: 32px; background: linear-gradient(#b0923f, #9d8032); border-radius: 6px; color: #2d2510; font-size: 17.5px; padding: 4px 0 0 8px; }
  .field-label { left: 21px; font-size: 12.5px; color: var(--ink); }
  .field { left: 21px; width: 193px; height: 23px; border: 1px solid var(--field-border); background: #fff; }
  .field-area { height: 60px; }
  .submit-btn { left: 47px; top: 1062px; width: 220px; height: 26px; background: linear-gradient(#b39540, #9c7f31); border-radius: 0 0 6px 6px; color: #2d2510; font-family: "Gelasio", Georgia, serif; font-size: 15.5px; padding: 3px 0 0 133px; display: flex; gap: 2px; align-items: center; }

  /* hero */
  .hero { left: 295px; top: 109px; width: 650px; height: 315px; background: linear-gradient(100deg, #e6dccb 0%, #f3ede1 35%, #d9cbb8 60%, #c5a68a 80%, #ece3d6 100%); }

  /* main column */
  .section-title { font-size: 19px; color: var(--ink); }
  .copy { font-size: 12px; line-height: 18.4px; color: var(--text); }
  .welcome-title { left: 295px; top: 444px; }
  .welcome-copy { left: 295px; top: 476px; width: 405px; }
  .testi-title { left: 295px; top: 661px; }
  .testimonial { left: 295px; width: 403px; border-bottom: 1px solid var(--rule); }
  .testimonial .copy { width: 405px; }
  .testi-author { text-align: right; color: var(--gold); font-size: 15px; padding: 4px 0 6px; }
  .read-more { left: 598px; top: 935px; width: 100px; text-align: right; font-size: 10px; color: var(--gold); }

  .awards { left: 295px; top: 976px; width: 404px; height: 112px; background: var(--panel); border-radius: 8px; }
  .award { position: absolute; }

  /* right column */
  .side-title { font-size: 18px; color: var(--ink); }
  .side-copy { font-size: 12px; line-height: 15px; color: var(--text); }
  .side-link { font-size: 10px; color: var(--gold); text-align: right; width: 196px; left: 749px; }
  .side-rule { left: 749px; width: 196px; height: 1px; background: var(--rule); }

  /* footer */
  .footer-rule { left: 40px; top: 1109px; width: 905px; height: 1px; background: #c8c8c8; }
  .footer-nav { left: 44px; top: 1117px; display: flex; gap: 25px; }
  .footer-nav a { color: var(--ink); text-decoration: none; font-size: 10px; }
  .footer-band { left: 40px; top: 1132px; width: 905px; height: 68px; }
  .copyright { left: 58px; top: 1165px; font-size: 10px; color: var(--ink); }
  .cards { left: 782px; top: 1133px; display: flex; gap: 2px; }
  .card { width: 39px; height: 25px; border: 1px solid #bbb; display: flex; align-items: center; justify-content: center; font-size: 7.5px; font-weight: 600; color: #fff; }
  .card-north { background: #3f7fbf; }
  .card-vera { background: #f1f1f1; color: #2b3f8c; }
  .card-meridian { background: #b33b2e; }
  .card-luma { background: #f4f4f4; color: #333; }
</style>
</head>
<body>

<svg class="abs header-band" viewBox="0 0 905 66" aria-hidden="true">
  <defs>
    <linearGradient id="goldBand" x1="0" y1="0" x2="0" y2="1">
      <stop offset="0" stop-color="#a98a3b"/>
      <stop offset="0.5" stop-color="#c9ab4b"/>
      <stop offset="1" stop-color="#e2c965"/>
    </linearGradient>
  </defs>
  <path d="M0 0 H905 V66 H520 C498 66 490 40 470 18 C460 8 448 8 430 8 H0 Z" fill="#dcdcdc"/>
  <path d="M0 0 H905 V60 H522 C502 60 494 36 474 14 C464 6 452 7 434 7 H0 Z" fill="url(#goldBand)"/>
</svg>

<div class="abs brand">
  <div class="brand-mark"></div>
  <div class="brand-name">Whitmore Law</div>
</div>

<nav class="abs main-nav">
  <a href="#">Home</a>
  <a href="#">Meet Our Attorney</a>
  <a href="#">FAQ</a>
  <a href="#">Contact Us</a>
</nav>

<h2 class="abs practice-title serif">Area Of Practice</h2>
<ul class="abs practice-list">
  <li>Family Law</li><li>Divorce</li><li>Alimony</li><li>Child Custody</li><li>Child Support</li>
  <li>Collaborative Divorce</li><li>Contested Divorce</li><li>Division of Assets</li><li>Domestic Violence</li>
  <li>Family/Relative Adoption</li><li>Fathers’ Rights</li><li>Grandparents’ Rights</li><li>Guardianship</li>
  <li>Legal Separation</li><li>Mediation</li><li>Modification of Spousal Support</li><li>Mothers’ Rights</li>
  <li>Palimony</li><li>Parental Alienation</li><li>Paternity</li><li>Prenuptial Agreements</li>
  <li>Postnuptial Agreements</li><li>Property Division</li><li>Relocation</li><li>Uncontested Divorce</li><li>Visitation</li>
</ul>

<form class="abs quick-contact">
  <h2 class="abs quick-title serif">Quick Contact</h2>
  <label class="abs field-label" style="top:57px">Name</label>
  <div class="abs field" style="top:73px"></div>
  <label class="abs field-label" style="top:98px">Email</label>
  <div class="abs field" style="top:114px"></div>
  <label class="abs field-label" style="top:140px">Phone</label>
  <div class="abs field" style="top:156px"></div>
  <label class="abs field-label" style="top:182px">Matter</label>
  <div class="abs field field-area" style="top:198px"></div>
</form>
<div class="abs submit-btn">Submit
  <svg width="18" height="12" viewBox="0 0 18 12" aria-hidden="true"><path d="M0 6 H16 M11 1 L16 6 L11 11" stroke="#fff" stroke-width="2" fill="none"/></svg>
</div>

<div class="abs hero" role="img" aria-label="Photo of an unhappy couple on a sofa, the woman in front resting her head on her hand"></div>

<h1 class="abs section-title serif welcome-title">Welcome to Whitmore</h1>
<p class="abs copy welcome-copy">Lorem Ipsum is simply dummy text of the printing and typesetting industry. Lorem Ipsum has been the industry's standard dummy text ever since the 1500s, when an unknown printer took a galley of type and scrambled it to make a type specimen book. It has survived not only five centuries, but also the leap into electronic typesetting, remaining essen-tially unchanged. It was popularised in the 1960s with the release of Letraset sheets containing Lorem Ipsum passages, and more recently with desktop publishing software like Aldus PageMaker including versions of Lorem Ipsum.</p>

<h2 class="abs section-title serif testi-title">Client Testimonials</h2>
<div class="abs testimonial" style="top:698px">
  <p class="copy">Lorem Ipsum is simply dummy text of the printing and typesetting industry. Lorem Ipsum has been the industry's standard dummy text ever since the 1500s, when an unknown printer took a galley of type and scrambled it to make a type specimen book.</p>
  <p class="testi-author">Daniel Reese</p>
</div>
<div class="abs testimonial" style="top:820px">
  <p class="copy">Lorem Ipsum is simply dummy text of the printing and typesetting industry. Lorem Ipsum has been the industry's standard dummy text ever since the 1500s, when an unknown printer took a galley of type and scrambled it to make a type specimen book.</p>
  <p class="testi-author">Daniel Reese</p>
</div>
<a class="abs read-more">read more</a>

<div class="abs awards">
  <div class="award" style="left:24px;top:30px;width:144px;height:60px;background:#d92f2a;border-radius:4px"></div>
  <div class="award" style="left:201px;top:29px;width:84px;height:57px;background:#8f9fcf;border-radius:3px"></div>
  <div class="award" style="left:325px;top:25px;width:41px;height:63px;background:#1f6e8c;border-radius:3px"></div>
</div>

<h2 class="abs side-title serif" style="left:749px;top:444px">Video Center</h2>
<svg class="abs" style="left:749px;top:473px" width="190" height="109" viewBox="0 0 190 109" aria-hidden="true">
  <defs>
    <linearGradient id="screen" x1="0" y1="0" x2="0" y2="1">
      <stop offset="0" stop-color="#555"/><stop offset="0.5" stop-color="#111"/><stop offset="1" stop-color="#000"/>
    </linearGradient>
  </defs>
  <rect x="0" y="0" width="190" height="109" rx="3" fill="#a9a9a9"/>
  <rect x="6" y="5" width="178" height="86" fill="url(#screen)"/>
  <path d="M77 30 L77 72 L125 51 Z" fill="#e8e8e8"/>
  <rect x="6" y="94" width="178" height="11" fill="#d8d8d8"/>
  <path d="M12 97 L17 99.5 L12 102 Z" fill="#444"/>
  <rect x="27" y="98" width="118" height="3" fill="#c33"/>
  <circle cx="67" cy="99.5" r="3" fill="#444"/>
  <rect x="170" y="97" width="6" height="5" fill="#444"/>
</svg>
<p class="abs side-copy" style="left:751px;top:590px;width:196px">Lorem Ipsum is simply dummy text of the printing and typesetting industry.</p>
<div class="abs side-rule" style="top:642px"></div>

<h2 class="abs side-title serif" style="left:750px;top:652px">Talk to us</h2>
<svg class="abs" style="left:746px;top:686px" width="82" height="58" viewBox="0 0 82 58" aria-hidden="true">
  <path d="M6 40 L24 10 H66 L78 40 V50 H6 Z" fill="#c9cdd2" stroke="#8b9096"/>
  <path d="M10 16 C10 6 72 6 72 16 L64 22 C60 16 22 16 18 22 Z" fill="#aeb3b9" stroke="#7d8288"/>
  <rect x="30" y="24" width="24" height="8" fill="#9fb9c9"/>
  <g fill="#7d8288"><circle cx="32" cy="38" r="2"/><circle cx="40" cy="38" r="2"/><circle cx="48" cy="38" r="2"/><circle cx="32" cy="44" r="2"/><circle cx="40" cy="44" r="2"/><circle cx="48" cy="44" r="2"/></g>
</svg>
<p class="abs side-copy" style="left:839px;top:687px;width:110px">Lorem Ipsum is simply dummy text of the printing</p>
<a class="abs side-link" style="top:752px">click here</a>
<div class="abs side-rule" style="top:771px"></div>

<h2 class="abs side-title serif" style="left:749px;top:781px">Case Evaluation</h2>
<svg class="abs" style="left:752px;top:812px" width="52" height="56" viewBox="0 0 52 56" aria-hidden="true">
  <path d="M4 4 H36 L44 12 V52 H4 Z" fill="#f4f4f4" stroke="#9a9a9a"/>
  <g stroke="#c4c4c4"><line x1="10" y1="16" x2="36" y2="16"/><line x1="10" y1="22" x2="36" y2="22"/><line x1="10" y1="28" x2="36" y2="28"/><line x1="10" y1="34" x2="30" y2="34"/></g>
  <path d="M18 42 L22 47 L30 38" stroke="#333" stroke-width="2" fill="none"/>
  <path d="M40 8 L48 10 L38 44 L34 46 L34 42 Z" fill="#444"/>
</svg>
<p class="abs side-copy" style="left:823px;top:818px;width:110px">Lorem Ipsum is simply dummy text of the printing</p>
<a class="abs side-link" style="top:871px">click here</a>
<div class="abs side-rule" style="top:886px"></div>

<div class="abs footer-rule"></div>
<nav class="abs footer-nav">
  <a href="#">Home</a><a href="#">Meet Our Attorney</a><a href="#">FAQ</a><a href="#">Contact Us</a>
</nav>
<svg class="abs footer-band" viewBox="0 0 905 68" aria-hidden="true">
  <defs>
    <linearGradient id="footGold" x1="0" y1="0" x2="0" y2="1">
      <stop offset="0" stop-color="#e2c965"/><stop offset="0.5" stop-color="#c9ab4b"/><stop offset="1" stop-color="#a98a3b"/>
    </linearGradient>
  </defs>
  <path d="M0 2 H392 C410 2 418 8 428 20 C444 40 456 58 480 58 H905 V68 H0 Z" fill="#dcdcdc"/>
  <path d="M0 6 H388 C404 6 412 12 422 24 C438 44 452 60 476 60 H905 V68 H0 Z" fill="url(#footGold)"/>
</svg>
<p class="abs copyright">© 2012 Whitmore,&nbsp; All Rights Reserved</p>
<div class="abs cards">
  <div class="card card-north">Northpay</div>
  <div class="card card-vera">Veracard</div>
  <div class="card card-meridian">Meridian</div>
  <div class="card card-luma">Lumacard</div>
</div>

</body>
</html>
```